Stationary/business card/envelope design for Larkvale Dentalcare

We are located in the foothills of the sierra nevada mountains. We are looking for a beautiful classy modern stationary. We need evelopes and business card design all to flow seamlessly. Envelope design.

Additional office address 4816 Meridian Wy., Suite B, Auburn, CA 95604 Phone: pending Fax: pending.

3 different Drs on each business card:
Helen R. Marsh, DDS
Orla P. Marsh, DDS
Rebecca S. Halvey, DDS

Target Market(s)

Dental patients

Industry/Entity Type

Dental

Contact Information for Business Card

Two sided. See example.

Font styles to use
Sans Serif

Requirements
Must have
• One sided business cards. Need envelope design.
Colors should match existing logo.

Helen R. Marsh, DDS
Orla P. Marsh, DDS
Rebecca S. Halvey, DDS

```html
<!DOCTYPE html>
<html lang="en">
<head>
<meta charset="utf-8">
<title>Larkvale Dentalcare – Business Card</title>
<link href="https://fonts.googleapis.com/css2?family=Roboto:wght@400;500&family=Tinos:ital,wght@1,700&display=swap" rel="stylesheet">
<style>
  :root {
    --backdrop: #8c8c8c;
    --card: #ffffff;
    --green: #137a3e;
    --blue: #2fb0dc;
    --ink: #3d3d3d;
  }
  html, body {
    margin: 0;
    padding: 0;
    width: 1200px;
    height: 1041px;
    overflow: hidden;
    background: var(--backdrop);
  }
  .canvas {
    position: relative;
    width: 1200px;
    height: 1041px;
    font-family: "Roboto", Arial, sans-serif;
    color: var(--ink);
  }
  .card {
    position: absolute;
    top: 152px;
    width: 388px;
    height: 701px;
    background: var(--card);
  }
  .card--front { left: 163px; }
  .card--back { left: 648px; }

  .brand {
    position: absolute;
    left: 0;
    width: 100%;
    text-align: center;
  }
  .brand__mark {
    display: block;
    margin: 0 auto 18px;
    border-radius: 50%;
    background: var(--blue);
  }
  .brand__name {
    display: block;
    font-weight: 500;
    color: var(--green);
    line-height: 1.25;
  }
  .card--front .brand { top: 58px; }
  .card--front .brand__mark { width: 150px; height: 150px; }
  .card--front .brand__name { font-size: 21px; }
  .card--back .brand { top: 60px; }
  .card--back .brand__mark { width: 128px; height: 128px; }
  .card--back .brand__name { font-size: 18px; }

  .doctor {
    position: absolute;
    top: 343px;
    left: 0;
    width: 100%;
    text-align: center;
    font-family: "Tinos", "Times New Roman", serif;
    font-style: italic;
    font-weight: 700;
  }
  .doctor__name {
    margin: 0;
    font-size: 31px;
    line-height: 36px;
    color: var(--green);
  }
  .doctor__specialty {
    margin: 0;
    font-size: 19px;
    line-height: 24px;
    color: var(--blue);
  }

  .contact {
    position: absolute;
    left: 37px;
    top: 440px;
    margin: 0;
    padding: 0;
    list-style: none;
    font-size: 19px;
    line-height: 24px;
  }
  .contact__item {
    position: relative;
    padding-left: 23px;
  }
  .contact__item--address { margin-bottom: 10px; }
  .contact__item--line { line-height: 25.5px; }
  .contact__icon {
    position: absolute;
    left: 0;
    top: 5px;
    width: 15px;
    height: 15px;
  }

  .appointment {
    position: absolute;
    left: 0;
    top: 290px;
    width: 100%;
    text-align: center;
    margin: 0;
    font-size: 21px;
    font-weight: 400;
    color: var(--green);
  }
  .slots {
    position: absolute;
    left: 56px;
    top: 342px;
    margin: 0;
    padding: 0;
    list-style: none;
    font-size: 19px;
  }
  .slot {
    display: flex;
    align-items: baseline;
    height: 55.5px;
  }
  .slot__day { width: 51px; }
  .slot__blank {
    display: inline-block;
    border-bottom: 1.2px solid var(--ink);
    height: 18px;
  }
  .slot__blank--date { width: 142px; }
  .slot__blank--time { width: 54px; }
  .slot__at { padding: 0 1px; }
  .notice {
    position: absolute;
    left: 0;
    top: 614px;
    width: 100%;
    text-align: center;
    margin: 0;
    font-size: 16.5px;
    line-height: 21px;
  }
</style>
</head>
<body>
<main class="canvas">

  <section class="card card--front" aria-label="Business card front">
    <div class="brand">
      <span class="brand__mark"></span>
      <span class="brand__name">Larkvale Dental Care<br>Corporation</span>
    </div>

    <div class="doctor">
      <p class="doctor__name">Helen R. Marsh, DDS</p>
      <p class="doctor__specialty">Family &amp; Cosmetic Dentistry</p>
    </div>

    <ul class="contact">
      <li class="contact__item contact__item--address">
        <svg class="contact__icon" viewBox="0 0 15 15"><rect x="1" y="1" width="13" height="13" fill="none" stroke="var(--green)" stroke-width="1.6"/></svg>
        5172 Cedar Ridge Road<br>Folsom,&nbsp; California&nbsp; 95631
      </li>
      <li class="contact__item contact__item--address">
        <svg class="contact__icon" viewBox="0 0 15 15"><rect x="1" y="1" width="13" height="13" fill="none" stroke="var(--green)" stroke-width="1.6"/></svg>
        4816 Meridian Wy., Suite B,<br>Auburn, CA 95604
      </li>
      <li class="contact__item contact__item--line">
        <svg class="contact__icon" viewBox="0 0 15 15"><path d="M1 6 Q7.5 0 14 6 L12 7.5 L10 6 L10 5 Q7.5 4 5 5 L5 6 L3 7.5 Z M3 9 L12 9 L13 14 L2 14 Z" fill="var(--green)"/></svg>
        (916) 555-0142
      </li>
      <li class="contact__item contact__item--line">
        <svg class="contact__icon" viewBox="0 0 15 15"><rect x="4" y="1" width="7" height="4" fill="var(--green)"/><rect x="1" y="5" width="13" height="6" fill="var(--green)"/><rect x="4" y="9" width="7" height="5" fill="#fff" stroke="var(--green)" stroke-width="1.4"/></svg>
        (916) 555-0187
      </li>
      <li class="contact__item contact__item--line">
        <svg class="contact__icon" viewBox="0 0 15 15"><rect x="1" y="3" width="13" height="9" fill="var(--green)"/><path d="M1.5 3.5 L7.5 8.5 L13.5 3.5 M1.5 11.5 L6 7 M13.5 11.5 L9 7" fill="none" stroke="#fff" stroke-width="1.1"/></svg>
        www.larkvaledentalcare.com
      </li>
      <li class="contact__item contact__item--line">
        <svg class="contact__icon" viewBox="0 0 15 15"><circle cx="7.5" cy="7.5" r="6.8" fill="var(--green)"/><path d="M4 4 Q6 3 7 5 Q6 7 4.5 7 Z M8.5 8 Q11 8 11 10.5 Q9.5 12.5 8 12 Z" fill="#fff"/></svg>
        larkvaledentalcare@mail.com
      </li>
    </ul>
  </section>

  <section class="card card--back" aria-label="Business card back">
    <div class="brand">
      <span class="brand__mark"></span>
      <span class="brand__name">Larkvale Dental Care<br>Corporation</span>
    </div>

    <h2 class="appointment">HAS AN APPOINTMENT ON</h2>

    <ul class="slots">
      <li class="slot"><span class="slot__day">Mon</span><span class="slot__blank slot__blank--date"></span><span class="slot__at">AT</span><span class="slot__blank slot__blank--time"></span></li>
      <li class="slot"><span class="slot__day">Tues</span><span class="slot__blank slot__blank--date"></span><span class="slot__at">AT</span><span class="slot__blank slot__blank--time"></span></li>
      <li class="slot"><span class="slot__day">Wed</span><span class="slot__blank slot__blank--date"></span><span class="slot__at">AT</span><span class="slot__blank slot__blank--time"></span></li>
      <li class="slot"><span class="slot__day">Thu</span><span class="slot__blank slot__blank--date"></span><span class="slot__at">AT</span><span class="slot__blank slot__blank--time"></span></li>
      <li class="slot"><span class="slot__day">Fri</span><span class="slot__blank slot__blank--date"></span><span class="slot__at">AT</span><span class="slot__blank slot__blank--time"></span></li>
    </ul>

    <p class="notice">IF UNABLE TO KEEP APPOINTMENT<br>KINDLY GIVE 24 HOUR NOTICE</p>
  </section>

</main>
</body>
</html>
```